RBT Core Values & Guiding Principles Visual System

Design a cohesive set of graphics that visually communicate RBT’s Core Values and Guiding Principles. The work includes a large wall sign, posters, simple icons for stickers and hard hats, a standard Guiding Principles graphic, and a clean email signature, all using a consistent, professional style suitable for an industrial environment.

Target Market(s)

This is mostly internal for employees

Industry/Entity Type

Construction

Requirements
Must have
• Edge and a clean but industrial feel
Nice to have
• See attached
Should not have
• Anything outside of the Brand Guide colors

```html
<!DOCTYPE html>
<html lang="en">
<head>
<meta charset="utf-8">
<title>RBT Core Values Visual System</title>
<link href="https://fonts.googleapis.com/css2?family=Montserrat:wght@500;600;700;800&family=Open+Sans:wght@400;600;700&display=swap" rel="stylesheet">
<style>
:root{
  --bg-top:#eceef4;
  --bg-bottom:#dfe2ec;
  --charcoal:#2f2f33;
  --charcoal-dark:#232326;
  --red:#d42a22;
  --red-dark:#a51b16;
  --steel:#5d5f66;
  --white:#ffffff;
  --ink:#3a3b44;
  --muted:#6a6c75;
}
*{margin:0;padding:0;box-sizing:border-box}
html,body{width:800px;height:1200px;overflow:hidden}
body{
  position:relative;
  background:linear-gradient(180deg,var(--bg-top),var(--bg-bottom));
  font-family:"Open Sans",sans-serif;color:var(--ink);
}
.icon-defs{position:absolute;width:0;height:0}

/* dimension marks */
.dim-width{position:absolute;left:48px;top:73px;width:710px;height:1px;background:#9a9ca4}
.dim-width span{position:absolute;left:50%;top:-9px;transform:translateX(-50%);background:var(--bg-top);padding:0 8px;font-size:13px;color:var(--muted)}
.dim-height{position:absolute;left:27px;top:94px;width:1px;height:225px;background:#9a9ca4}
.dim-height span{position:absolute;left:-12px;top:100px;background:var(--bg-top);padding:4px 0;font-size:13px;color:var(--muted)}

/* wall sign */
.wall-sign{
  position:absolute;left:48px;top:94px;width:710px;height:225px;
  background:linear-gradient(135deg,#3a3a3e,var(--charcoal-dark));
  box-shadow:0 6px 14px rgba(0,0,0,.25);overflow:hidden;
}
.wall-sign__band{position:absolute;left:0;top:0;width:69px;height:100%;background:linear-gradient(180deg,var(--red),var(--red-dark))}
.wall-sign__title{position:absolute;left:0;right:0;top:22px;display:flex;justify-content:center;align-items:center;gap:12px;padding-left:40px}
.brand-dot{display:inline-block;border-radius:50%;background:var(--red)}
.wall-sign__title .brand-dot{width:36px;height:36px}
.wall-sign__title h1{font-family:"Montserrat",sans-serif;font-weight:800;font-size:38px;color:var(--white);letter-spacing:1px}
.wall-sign__values{position:absolute;left:200px;top:76px;width:505px;display:flex}
.wall-value{flex:1;text-align:center;border-left:1px solid rgba(255,255,255,.12);height:112px}
.wall-value:first-child{border-left:none}
.wall-value svg{width:52px;height:57px;margin-top:10px}
.wall-value p{font-family:"Montserrat",sans-serif;font-weight:500;font-size:11px;line-height:16px;color:var(--white);margin-top:10px;letter-spacing:-.3px}
.wall-sign__tagline{position:absolute;left:178px;right:0;top:203px;height:22px;background:var(--red);color:var(--white);font-size:13px;letter-spacing:1px;line-height:22px;padding-left:82px}

/* posters */
.posters{position:absolute;left:8px;top:454px;width:784px;height:260px}
.poster{position:absolute;top:0;width:149px;height:221px;background:linear-gradient(160deg,#3b3b3f,var(--charcoal-dark));box-shadow:0 4px 10px rgba(0,0,0,.25);text-align:center;color:var(--white)}
.poster svg{width:78px;height:86px;margin-top:18px}
.poster h2{font-family:"Montserrat",sans-serif;font-size:17px;line-height:24px;margin-top:14px;letter-spacing:-.5px}
.poster h2 .light{font-weight:500;display:block}
.poster h2 .bold{font-weight:800;display:block}
.poster p{font-size:7px;line-height:8px;font-weight:600;margin:8px 8px 0}
.poster-size{position:absolute;top:244px;width:149px;text-align:center;font-size:10px;color:var(--muted)}

/* stickers */
.stickers{position:absolute;left:0;top:748px;width:800px;height:120px}
.sticker{position:absolute;top:0;width:114px;height:114px}
.stickers-label{position:absolute;left:0;width:705px;top:878px;text-align:center;font-size:11px;color:var(--muted)}

/* guiding principles */
.principles{position:absolute;left:18px;top:906px;width:162px;background:var(--charcoal);box-shadow:0 3px 8px rgba(0,0,0,.25);border-radius:2px}
.principles h3{background:var(--red);color:var(--white);font-size:10px;font-weight:700;padding:5px 8px;letter-spacing:.2px}
.principles ul{list-style:none;padding:5px 8px 6px}
.principles li{color:var(--white);font-size:12.5px;line-height:21.5px;display:flex;align-items:center;gap:6px}
.principles li svg{width:13px;height:13px;flex:none}
.principles li strong{font-weight:700}

/* hard hat decal (flat) */
.hat-decal{position:absolute;left:200px;top:1000px;display:flex;align-items:center;gap:10px}
.hat-decal .brand-dot{width:34px;height:34px}
.hat-decal span{font-family:"Montserrat",sans-serif;font-weight:700;font-size:40px;color:var(--charcoal-dark)}

/* email signature */
.signature{position:absolute;left:484px;top:900px;width:310px}
.signature__brand{display:flex;align-items:center;gap:8px}
.signature__brand .brand-dot{width:24px;height:24px}
.signature__brand span{font-family:"Montserrat",sans-serif;font-weight:600;font-size:26px;color:var(--charcoal)}
.signature__name{font-family:"Montserrat",sans-serif;font-weight:800;font-size:21px;color:var(--red-dark);margin-top:6px}
.signature__role{font-size:13px;color:var(--muted);margin-top:1px}
.signature__principles{margin-top:50px;font-size:14px;line-height:19px;color:var(--ink);font-weight:600;letter-spacing:-.2px}
.signature__principles .sep{color:var(--red);margin:0 4px}
.signature__principles .soft{font-weight:400}
</style>
</head>
<body>

<svg class="icon-defs" aria-hidden="true">
  <defs>
    <symbol id="shield" viewBox="0 0 100 110">
      <path d="M50 4 L94 16 L89 64 Q80 94 50 108 Q20 94 11 64 L6 16 Z" fill="#6a6c72"/>
      <path d="M50 4 L88 15 L84 52 Q76 80 50 92 Q24 80 16 52 L12 15 Z" fill="#d42a22"/>
    </symbol>
    <symbol id="icon-check" viewBox="0 0 100 110">
      <use href="#shield"/>
      <path d="M32 30 L68 30 L68 50 Q66 64 50 72 Q34 64 32 50 Z" fill="#fff"/>
      <path d="M40 48 L48 56 L60 40" fill="none" stroke="#2f2f33" stroke-width="5"/>
    </symbol>
    <symbol id="icon-helmet" viewBox="0 0 100 110">
      <use href="#shield"/>
      <path d="M28 58 Q28 28 50 28 Q72 28 72 58 Z" fill="#fff"/>
      <rect x="24" y="56" width="52" height="7" rx="3" fill="#fff"/>
      <path d="M36 66 Q50 80 64 66" fill="none" stroke="#fff" stroke-width="5"/>
    </symbol>
    <symbol id="icon-clipboard" viewBox="0 0 100 110">
      <use href="#shield"/>
      <rect x="30" y="24" width="36" height="46" rx="3" fill="#fff"/>
      <path d="M37 36 H59 M37 45 H59 M37 54 H52" stroke="#d42a22" stroke-width="4"/>
      <path d="M52 62 L60 70 L78 50" fill="none" stroke="#fff" stroke-width="6"/>
    </symbol>
    <symbol id="icon-mountain" viewBox="0 0 100 110">
      <use href="#shield"/>
      <path d="M20 66 L42 30 L52 46 L60 36 L82 66 L60 52 L52 60 L44 48 Z" fill="#fff"/>
    </symbol>
    <symbol id="icon-fist" viewBox="0 0 100 110">
      <use href="#shield"/>
      <rect x="32" y="28" width="36" height="42" rx="8" fill="#fff"/>
      <path d="M41 28 V44 M50 28 V44 M59 28 V44 M32 50 H60" stroke="#d42a22" stroke-width="3"/>
    </symbol>
    <symbol id="icon-arrow" viewBox="0 0 100 110">
      <use href="#shield"/>
      <path d="M24 72 L62 36 L54 28 L80 24 L76 50 L68 42 L30 78 Z" fill="#fff"/>
    </symbol>
  </defs>
</svg>

<div class="dim-width"><span>17 ft</span></div>
<div class="dim-height"><span>4 ft</span></div>

<section class="wall-sign">
  <div class="wall-sign__band"></div>
  <div class="wall-sign__title"><i class="brand-dot"></i><h1>RBT CORE VALUES</h1></div>
  <div class="wall-sign__values">
    <div class="wall-value"><svg><use href="#icon-check"/></svg><p>UNCOMPROMIS<br>SAFETY</p></div>
    <div class="wall-value"><svg><use href="#icon-clipboard"/></svg><p>RELENTLESS<br>DISCIPLINE</p></div>
    <div class="wall-value"><svg><use href="#icon-mountain"/></svg><p>EMBRACE<br>THE HARD</p></div>
    <div class="wall-value"><svg><use href="#icon-fist"/></svg><p>OWN<br>IT</p></div>
    <div class="wall-value"><svg><use href="#icon-arrow"/></svg><p>FORWARD<br>ALWAYS</p></div>
  </div>
  <div class="wall-sign__tagline">Improving the environment and people's lives.</div>
</section>

<section class="posters">
  <article class="poster" style="left:0"><svg><use href="#icon-helmet"/></svg><h2><span class="light">UNCOMPROMIS</span><span class="bold">SAFETY</span></h2><p>We champion an unwavering commitment to safety. Protecting people is our top priority – always above production, profit, or pressure.</p></article>
  <article class="poster" style="left:162px"><svg><use href="#icon-clipboard"/></svg><h2><span class="light">RELENTLESS</span><span class="bold">DISCIPLINE</span></h2><p>We are committed to excellence through consistency, precision, and steadfast refusal to cut corners.</p></article>
  <article class="poster" style="left:324px"><svg><use href="#icon-mountain"/></svg><h2><span class="light">EMBRACE</span><span class="bold">THE HARD</span></h2><p>We are committed to excellence through consistency, precision, and steadfast refusal to cut corners.</p></article>
  <article class="poster" style="left:485px"><svg><use href="#icon-fist"/></svg><h2><span class="light">OWN</span><span class="bold">IT</span></h2><p>We are committed to excellence through consistency, precision, and steadfast refusal to cut corners.</p></article>
  <article class="poster" style="left:644px"><svg><use href="#icon-arrow"/></svg><h2><span class="light">FORWARD</span><span class="bold">ALWAYS</span></h2><p>We are committed to excellence through consistency, precision, and steadfast refusal to cut corners.</p></article>
  <span class="poster-size" style="left:0">24 x 36 in</span>
  <span class="poster-size" style="left:162px">24 x 36 in</span>
  <span class="poster-size" style="left:324px">24 x 36 in</span>
  <span class="poster-size" style="left:485px">24 x 36 in</span>
  <span class="poster-size" style="left:644px">24 x 36 in</span>
</section>

<section class="stickers">
  <svg class="sticker" style="left:23px" viewBox="0 0 114 114">
    <defs><path id="arc-top" d="M17 57 A40 40 0 0 1 97 57"/><path id="arc-bottom" d="M14 57 A43 43 0 0 0 100 57"/></defs>
    <circle cx="57" cy="57" r="55" fill="#fff"/><circle cx="57" cy="57" r="52" fill="#2f2f33" stroke="#d42a22" stroke-width="2"/>
    <text font-family="Montserrat,sans-serif" font-weight="800" font-size="11" fill="#fff"><textPath href="#arc-top" startOffset="50%" text-anchor="middle">UNCOMPROMISED</textPath></text>
    <text font-family="Montserrat,sans-serif" font-weight="800" font-size="11" fill="#fff"><textPath href="#arc-bottom" startOffset="50%" text-anchor="middle">SAFETY</textPath></text>
    <svg x="32" y="28" width="50" height="55"><use href="#icon-helmet"/></svg>
  </svg>
  <svg class="sticker" style="left:133px" viewBox="0 0 114 114">
    <circle cx="57" cy="57" r="55" fill="#fff"/><circle cx="57" cy="57" r="52" fill="#2f2f33" stroke="#d42a22" stroke-width="2"/>
    <text font-family="Montserrat,sans-serif" font-weight="800" font-size="11" fill="#fff"><textPath href="#arc-top" startOffset="50%" text-anchor="middle">RELENTLESS</textPath></text>
    <text font-family="Montserrat,sans-serif" font-weight="800" font-size="11" fill="#fff"><textPath href="#arc-bottom" startOffset="50%" text-anchor="middle">DISCIPLINE</textPath></text>
    <svg x="32" y="28" width="50" height="55"><use href="#icon-clipboard"/></svg>
  </svg>
  <svg class="sticker" style="left:242px" viewBox="0 0 114 114">
    <circle cx="57" cy="57" r="55" fill="#fff"/><circle cx="57" cy="57" r="52" fill="#2f2f33" stroke="#d42a22" stroke-width="2"/>
    <text font-family="Montserrat,sans-serif" font-weight="800" font-size="11" fill="#fff"><textPath href="#arc-top" startOffset="50%" text-anchor="middle">EMBRACE</textPath></text>
    <text font-family="Montserrat,sans-serif" font-weight="800" font-size="11" fill="#fff"><textPath href="#arc-bottom" startOffset="50%" text-anchor="middle">THE HARD</textPath></text>
    <svg x="32" y="28" width="50" height="55"><use href="#icon-mountain"/></svg>
  </svg>
  <svg class="sticker" style="left:350px" viewBox="0 0 114 114">
    <circle cx="57" cy="57" r="55" fill="#fff"/><circle cx="57" cy="57" r="52" fill="#2f2f33" stroke="#d42a22" stroke-width="2"/>
    <text font-family="Montserrat,sans-serif" font-weight="800" font-size="11" fill="#fff"><textPath href="#arc-top" startOffset="50%" text-anchor="middle">OWN IT</textPath></text>
    <svg x="32" y="28" width="50" height="55"><use href="#icon-fist"/></svg>
  </svg>
  <svg class="sticker" style="left:465px" viewBox="0 0 114 114">
    <circle cx="57" cy="57" r="55" fill="#fff"/><circle cx="57" cy="57" r="52" fill="#2f2f33" stroke="#d42a22" stroke-width="2"/>
    <text font-family="Montserrat,sans-serif" font-weight="800" font-size="11" fill="#fff"><textPath href="#arc-top" startOffset="50%" text-anchor="middle">FORWARD</textPath></text>
    <text font-family="Montserrat,sans-serif" font-weight="800" font-size="11" fill="#fff"><textPath href="#arc-bottom" startOffset="50%" text-anchor="middle">ALWAYS</textPath></text>
    <svg x="32" y="28" width="50" height="55"><use href="#icon-arrow"/></svg>
  </svg>
</section>
<p class="stickers-label">3 in stickers</p>

<section class="principles">
  <h3>RBT'S GUIDING PRINCIPLES</h3>
  <ul>
    <li><svg viewBox="0 0 14 14"><rect width="14" height="14" fill="#d42a22"/><path d="M3 7 L6 10 L11 4" fill="none" stroke="#fff" stroke-width="2"/></svg><strong>Guided by Safety</strong></li>
    <li><svg viewBox="0 0 14 14"><circle cx="7" cy="7" r="5" fill="none" stroke="#fff" stroke-width="3" stroke-dasharray="2 1.4"/><circle cx="7" cy="7" r="2" fill="#fff"/></svg>Prepared to Perform</li>
    <li><svg viewBox="0 0 14 14"><rect x="2" y="1" width="10" height="12" fill="#fff"/><path d="M4 4 H10 M4 7 H10 M4 10 H8" stroke="#2f2f33" stroke-width="1.2"/></svg>Disciplined to Deliver</li>
    <li><svg viewBox="0 0 14 14"><path d="M7 1 L8.8 5.2 L13 5.5 L9.8 8.4 L10.8 13 L7 10.6 L3.2 13 L4.2 8.4 L1 5.5 L5.2 5.2 Z" fill="#fff"/></svg>Committed to Quality</li>
  </ul>
</section>

<div class="hat-decal"><i class="brand-dot"></i><span>RBT</span></div>

<section class="signature">
  <div class="signature__brand"><i class="brand-dot"></i><span>RBT</span></div>
  <p class="signature__name">Dana Whitfield</p>
  <p class="signature__role">Project Manager</p>
  <p class="signature__principles">Guided by Safety<span class="sep">|</span>Prepared to Perform<br>Disciplined to Deliver<span class="sep">|</span>Committed <span class="soft">to Quality</span></p>
</section>

</body>
</html>
```